Brightwell Bonds and Households Initiative

We need a flyer that invites low-income Spanish speaking individuals to our program. The program is 12 weeks. We offer healthy relationship education, and financial stability. We also touch on workforce development. These workshops are for couples only.

We are in five locations, so we need a flyer that we can change the text to be able to update the address, dates and any additional information based on our needs.

Attached is the logo we would like to use. I have also attached a previous flyer that we created to give you an idea of the text that is included.

Target Market(s)

We are reaching out to low income adult couples

Font styles to use
Serif

Requirements
Must have
• This flyer must catch the eye of couples wanting to improve their relationship, and finances.
Nice to have
• Some space for us to plug in dates location and times. This flyer also has to have our funding statement at the bottom.

```html
<!DOCTYPE html>
<html lang="es">
<head>
<meta charset="utf-8">
<title>Lazos y Hogares Brightwell – Talleres</title>
<link href="https://fonts.googleapis.com/css2?family=Lora:wght@400;500;600;700&family=Libre+Baskerville:wght@400;700&family=Courgette&display=swap" rel="stylesheet">
<style>
  :root{
    --navy:#1e3a5f;
    --orange:#f39325;
    --orange-deep:#e8821a;
    --white:#ffffff;
    --paper:#fbfbfc;
    --ink:#1f2f46;
  }
  *{margin:0;padding:0;box-sizing:border-box}
  html,body{width:910px;height:1200px;overflow:hidden;background:var(--paper)}
  .flyer{position:relative;width:910px;height:1200px;overflow:hidden;background:var(--white);font-family:"Lora",Georgia,serif;color:var(--navy)}

  .backdrop{position:absolute;left:0;top:700px;width:910px;height:500px;
    background:radial-gradient(ellipse at 65% 70%, #e9ebef 0%, #f4f5f7 45%, rgba(255,255,255,0) 75%)}

  .brand{position:absolute;left:0;top:118px;width:910px;text-align:center}
  .brand-name{display:inline-flex;align-items:center;gap:14px;font-family:"Lora",Georgia,serif;font-weight:500;font-size:44px;color:var(--orange)}
  .brand-dot{width:22px;height:22px;border-radius:50%;background:var(--navy)}
  .brand-rule{width:560px;height:2px;background:var(--orange);margin:6px auto 8px}
  .brand-tagline{font-family:"Libre Baskerville",Georgia,serif;font-variant:small-caps;font-weight:700;font-size:19px;line-height:1.3;color:var(--navy)}

  .program-box{position:absolute;left:93px;top:276px;width:632px;height:128px;border:3px solid var(--navy);border-radius:26px;background:var(--white);text-align:center;padding-top:22px;z-index:3}
  .program-title{font-weight:700;font-size:27px;color:var(--navy)}
  .program-audience{font-family:"Courgette",cursive;font-size:22px;color:var(--orange);margin-top:6px}

  .schedule{position:absolute;left:93px;top:421px;width:620px;height:358px;background:var(--navy);border-radius:34px 0 190px 34px;color:var(--white);text-align:center;z-index:2;padding-top:34px}
  .schedule-group{width:520px;margin:0 0 0 100px}
  .schedule-label{font-weight:700;font-size:31px;color:var(--orange);line-height:1.15}
  .schedule-value{font-weight:700;font-size:21px;line-height:1.3}
  .schedule-rule{width:180px;height:2px;background:var(--orange);margin:12px auto 10px}
  .schedule-place{font-weight:700;font-size:16px;line-height:1.35}
  .schedule-phone{font-weight:700;font-size:21px;color:var(--orange);margin-top:10px}

  .care-note{position:absolute;left:864px;top:330px;height:410px;writing-mode:vertical-rl;font-weight:700;font-size:15.5px;color:var(--orange-deep);text-align:center}

  .topics{position:absolute;left:121px;top:792px;width:520px;z-index:2}
  .topics-heading{font-weight:700;font-size:17px;color:var(--navy);margin-bottom:4px}
  .topics-list{list-style:none}
  .topics-list li{position:relative;padding-left:26px;font-size:16.5px;line-height:27.5px;color:var(--navy)}
  .topics-list li::before{content:"";position:absolute;left:4px;top:10px;width:9px;height:9px;background:var(--navy)}

  .partner{position:absolute;z-index:2;display:flex;align-items:center;gap:10px;font-weight:700}
  .partner-center{left:672px;top:835px;width:220px;font-size:19px;line-height:1.15;color:var(--orange-deep)}
  .partner-uplift{left:660px;top:945px;width:230px;font-size:19px;line-height:1.15;color:var(--navy)}
  .partner-mark{flex:0 0 auto;width:30px;height:30px;border-radius:50%;background:var(--orange)}
  .partner-uplift .partner-mark{background:var(--navy)}

  .register{position:absolute;left:86px;top:1041px;width:400px;height:112px;background:var(--orange);border-radius:0 44px 44px 0;padding:12px 0 0 34px;color:var(--white);z-index:3}
  .register-call{font-weight:700;font-size:16.5px;color:var(--navy)}
  .register-info{font-size:15.5px;line-height:1.3}

  .funding{position:absolute;left:535px;top:1066px;width:352px;font-size:10.5px;line-height:1.4;font-weight:600;color:var(--ink);text-align:center;z-index:2}
</style>
</head>
<body>
<main class="flyer">
  <div class="backdrop" role="img" aria-label="Soft faded photograph of two hands reaching toward each other"></div>

  <header class="brand">
    <div class="brand-name"><span class="brand-dot"></span>Lazos y Hogares Brightwell</div>
    <div class="brand-rule"></div>
    <p class="brand-tagline">Fortalecimiento de Relaciones | Capacitación Financiera<br>y Preparación Laboral</p>
  </header>

  <section class="program-box">
    <h1 class="program-title">Brightwell Bonds and Households Initiative</h1>
    <p class="program-audience">We are reaching out to low income adult couples</p>
  </section>

  <section class="schedule">
    <div class="schedule-group">
      <h2 class="schedule-label">Fecha de talleres:</h2>
      <p class="schedule-value">jueves octubre 03, 12, 19, 26</p>
      <div class="schedule-rule"></div>
      <h2 class="schedule-label">Horario:</h2>
      <p class="schedule-value">5:30pm –8:00pm</p>
      <div class="schedule-rule"></div>
      <h2 class="schedule-label">Ubicación:</h2>
      <p class="schedule-place">Cedar Grove Family Resource Center<br>2250 Willow Ave, Lindale CA 90210</p>
      <p class="schedule-phone">(555) 214-0391</p>
    </div>
  </section>

  <p class="care-note">*Cuidado de niños y cena será proporcionado</p>

  <section class="topics">
    <h3 class="topics-heading">Temas incluyen:</h3>
    <ul class="topics-list">
      <li>Llaves para la buena communicación</li>
      <li>Tipos de personalidad y expectativas</li>
      <li>Señales de peligro en una relación</li>
      <li>Técnicas para formar y &nbsp;sostener una relación sana</li>
      <li>Resolucion de problemas</li>
      <li>Como mantener la diversion</li>
      <li>Como adminstrar el dinero entre pareja y muchos mas</li>
    </ul>
  </section>

  <div class="partner partner-center"><span class="partner-mark"></span>Cedar Grove Family Resource Center</div>
  <div class="partner partner-uplift"><span class="partner-mark"></span>Community Uplift Alliance</div>

  <section class="register">
    <p class="register-call">Registración requerida Llámanos hoy!</p>
    <p class="register-info">Para más información llame a<br>Cedar Grove Family Resource Center<br>(555) 214-0388</p>
  </section>

  <p class="funding">“Funding for this project was provided by the National Family Services Office, Bureau for Children and Households. Grant: #40BW2207. These services are available to all eligible persons, regardless of race, gender, age, disability, or religion.”</p>
</main>
</body>
</html>
```